METAL FABRICATION BUSINESS CARD

** I will be ending the project and picking design early. This Friday October 3rd at 7am MST if not sooner**
ONE SIDED BUSINESS CARD ONLY. AND LOGO SIZE TO BE DOMINANT so it stands out.
Looking for a black background and will be doing raised chrome/silver font on the business cards. Looking to have the following on the front of the business card. Company logo is uploaded in files.
Company logo
*Compartment Doors
*Roof Radius Metal
*J-Wrap Metal Skirting
*S-Lock Beltline Molding
*Pre-Bent Molding
and more...
Owen Baskell 406.529.1847 info@Trelvo-Works.com
Updates
One sided business card only please. Also logo size should be dominant and sized bigger
Contact Information for Business Card
Black background, Text will be raised chrome/silver, and corners will be rounded.

```html
<!DOCTYPE html>
<html lang="en">
<head>
<meta charset="UTF-8">
<title>Trelvo-Works Business Card</title>
<link rel="stylesheet" href="https://fonts.googleapis.com/css2?family=Montserrat:wght@400;500;700;800&display=swap">
<style>
  :root {
    --page-bg: #2a2a2a;
    --card-bg: #0c0c0c;
    --silver: #d6d6d6;
    --silver-soft: #b9b9b9;
    --texture-dark: #151515;
    --texture-light: #3a3a3a;
  }
  * { margin: 0; padding: 0; box-sizing: border-box; }
  html, body {
    width: 1200px;
    height: 875px;
    overflow: hidden;
    background: var(--page-bg);
    font-family: "Montserrat", sans-serif;
  }
  .canvas {
    width: 1200px;
    height: 875px;
    display: flex;
    align-items: center;
    justify-content: center;
  }
  .business-card {
    position: relative;
    width: 980px;
    height: 560px;
    background: var(--card-bg);
    border-radius: 26px;
    overflow: hidden;
    color: var(--silver);
    box-shadow: 0 20px 50px rgba(0,0,0,0.5);
  }
  .edge-texture {
    position: absolute;
    left: 0;
    top: 0;
    width: 150px;
    height: 100%;
    background: linear-gradient(90deg, var(--texture-light) 0%, var(--texture-dark) 55%, transparent 100%);
    opacity: 0.7;
  }
  .brand {
    position: absolute;
    left: 70px;
    top: 150px;
    display: flex;
    align-items: center;
    gap: 18px;
  }
  .brand-dot {
    width: 54px;
    height: 54px;
    border-radius: 50%;
    background: var(--silver);
  }
  .brand-name {
    font-weight: 800;
    font-size: 66px;
    letter-spacing: 1px;
    color: var(--silver);
  }
  .services {
    position: absolute;
    right: 70px;
    top: 56px;
    text-align: right;
  }
  .services-title {
    font-weight: 700;
    font-size: 22px;
    margin-bottom: 10px;
  }
  .services-list { list-style: none; }
  .services-list li {
    font-weight: 500;
    font-size: 19px;
    line-height: 1.5;
    color: var(--silver);
  }
  .services-list li::after {
    content: "";
    display: inline-block;
    width: 6px;
    height: 6px;
    margin-left: 10px;
    border-radius: 50%;
    background: var(--silver);
    vertical-align: middle;
  }
  .contact {
    position: absolute;
    left: 150px;
    bottom: 70px;
  }
  .contact-name {
    font-weight: 800;
    font-size: 28px;
    color: var(--silver);
  }
  .contact-role {
    font-size: 16px;
    color: var(--silver-soft);
    margin-bottom: 18px;
  }
  .contact-list { list-style: none; }
  .contact-list li {
    display: flex;
    align-items: center;
    gap: 12px;
    font-size: 18px;
    line-height: 1.55;
    color: var(--silver);
  }
  .contact-list svg { width: 16px; height: 16px; fill: var(--silver); }
</style>
</head>
<body>
<main class="canvas">
  <article class="business-card">
    <div class="edge-texture" role="img" aria-label="Dark hammered metal texture along the left edge"></div>

    <div class="brand">
      <span class="brand-dot"></span>
      <span class="brand-name">Trelvo-Works</span>
    </div>

    <section class="services">
      <h2 class="services-title">Oure Services</h2>
      <ul class="services-list">
        <li>Compartment Doors</li>
        <li>Roof Radius Metal</li>
        <li>J-Wrap Metal Skirting</li>
        <li>S-Lock Beltline Molding</li>
        <li>Pre-Bent Molding</li>
      </ul>
    </section>

    <section class="contact">
      <p class="contact-name">Owen Baskell</p>
      <p class="contact-role">Owner</p>
      <ul class="contact-list">
        <li>
          <svg viewBox="0 0 16 16" aria-hidden="true"><path d="M3 1h3l1.5 4-2 1.2a8 8 0 0 0 4.3 4.3L11 8.5l4 1.5v3c0 1-1 2-2 2A12 12 0 0 1 1 3c0-1 1-2 2-2z"/></svg>
          406.529.1847
        </li>
        <li>
          <svg viewBox="0 0 16 16" aria-hidden="true"><path d="M1 3h14v10H1z M2 4l6 5 6-5" fill="none" stroke="#d6d6d6" stroke-width="1.5"/></svg>
          info@Trelvo-Works.com
        </li>
        <li>
          <svg viewBox="0 0 16 16" aria-hidden="true"><circle cx="8" cy="8" r="7"/></svg>
          www.Trelvo-Works.com
        </li>
      </ul>
    </section>
  </article>
</main>
</body>
</html>
```